New Business Card Design Project

I need a design for business cards, i am an electrical business called "Vantor Electrical and Communications" i need the cards to be double sided with the company logo on the back (attached) the front needs to say my company name, web site, email address, telephone number, and ABN number and electrical license number. I am open to different arrangements of the information but would like the background to be incorporating something electrical or something that looks smart. open to all additional ideas also.

The company colours are orange and grey see logo attached.

Business Name: Vantor Electrical and Communications
Website: vantorelectricalandcomms.example.au
Email: dean@vantorelectricalandcomms.example.au
Telephone(mobile): 0481290736
ABN: 71829304516
Lic No: 483027D

Target Market(s)

Business entities, Project Managers, Accounts, Clients

Industry/Entity Type

Electrician

Contact Information for Business Card

I need a design for business cards, i am an electrical business called "Vantor Electrical and Communications" i need the cards to be double sided with the company logo on the back (attached) the front needs to say my company name

Font styles to use
Serif
Sans Serif

Colors
f37122
5c5c5c

Requirements
Must have
• Must have the Logo on the back open to different ways of it being on the back but had in mind to keep it central but again open to other options
Nice to have
• A real modern cool background that is eye catching yet contemporary
Should not have
• No backgrounds of a light bulb or plug or anything like that

```html
<!DOCTYPE html>
<html lang="en">
<head>
<meta charset="utf-8">
<title>Vantor Electrical and Communications – Business Cards</title>
<link rel="stylesheet" href="https://fonts.googleapis.com/css2?family=Ubuntu:wght@400;500&display=swap">
<style>
  :root {
    --page-bg: #e4e2de;
    --card-white: #f7f7f6;
    --band-grey: #5f5f61;
    --back-grey-light: #66666a;
    --back-grey-dark: #4a4a4d;
    --text-grey: #5c5c5c;
    --accent: #f2bd1d;
    --logo-white: #f4f4f4;
  }
  * { margin: 0; padding: 0; box-sizing: border-box; }
  html, body {
    width: 1200px; height: 780px; overflow: hidden;
    background: var(--page-bg);
    font-family: "Ubuntu", "Helvetica Neue", Arial, sans-serif;
  }
  .canvas {
    position: relative; width: 1200px; height: 780px;
  }
  .card {
    position: absolute; top: 235px;
    width: 540px; height: 309px;
    border-radius: 3px;
    box-shadow: 0 6px 18px rgba(0,0,0,.18);
    overflow: hidden;
  }

  /* Front */
  .card-front { left: 40px; background: var(--card-white); }
  .front-band {
    position: absolute; left: 0; top: 0; bottom: 0; width: 120px;
    background: var(--band-grey);
    display: flex; align-items: center; justify-content: center;
  }
  .front-band .brand-name {
    transform: rotate(-90deg);
    white-space: nowrap;
    color: var(--logo-white);
    font-weight: 400; font-size: 19px; letter-spacing: 1px;
    text-align: center; line-height: 1.3;
  }
  .front-content {
    position: absolute; left: 160px; top: 112px; right: 30px;
    color: var(--text-grey);
  }
  .person-name { font-size: 25px; font-weight: 400; line-height: 1; }
  .person-role { font-size: 16px; color: var(--accent); margin-top: 3px; }
  .contact-list { list-style: none; margin-top: 14px; }
  .contact-list li {
    display: flex; align-items: center; gap: 7px;
    font-size: 14.5px; line-height: 22px;
  }
  .contact-icon { width: 15px; height: 15px; flex: none; }
  .reg-line { font-size: 14.5px; margin-top: 10px; }
  .reg-line .label { color: var(--accent); }
  .licence {
    position: absolute; right: 26px; bottom: 22px;
    font-size: 14.5px; color: var(--text-grey);
  }
  .licence .label { color: var(--accent); }

  /* Back */
  .card-back {
    left: 620px;
    background: radial-gradient(ellipse at 45% 40%, var(--back-grey-light), var(--back-grey-dark));
    display: flex; align-items: center; justify-content: center;
  }
  .card-back .brand-name {
    color: var(--logo-white);
    font-weight: 400; font-size: 30px; letter-spacing: 1px;
    text-align: center; line-height: 1.3;
  }
</style>
</head>
<body>
<main class="canvas">

  <section class="card card-front" aria-label="Business card front">
    <div class="front-band">
      <p class="brand-name">Vantor<br>Electrical and Communications</p>
    </div>
    <div class="front-content">
      <p class="person-name">Employee Name</p>
      <p class="person-role">Principal</p>
      <ul class="contact-list">
        <li>
          <svg class="contact-icon" viewBox="0 0 16 16" aria-hidden="true">
            <rect width="16" height="16" rx="2" fill="var(--accent)"/>
            <rect x="5" y="3" width="6" height="10" rx="1" fill="none" stroke="#fff" stroke-width="1.3"/>
            <circle cx="8" cy="11.2" r=".7" fill="#fff"/>
          </svg>
          0481290736
        </li>
        <li>
          <svg class="contact-icon" viewBox="0 0 16 16" aria-hidden="true">
            <rect width="16" height="16" rx="2" fill="var(--accent)"/>
            <rect x="3" y="4.5" width="10" height="7" fill="none" stroke="#fff" stroke-width="1.2"/>
            <path d="M3 4.5 L8 9 L13 4.5" fill="none" stroke="#fff" stroke-width="1.2"/>
          </svg>
          dean@vantorelectricalandcomms.example.au
        </li>
        <li>
          <svg class="contact-icon" viewBox="0 0 16 16" aria-hidden="true">
            <rect width="16" height="16" rx="2" fill="var(--accent)"/>
            <circle cx="8" cy="8" r="5" fill="none" stroke="#fff" stroke-width="1.1"/>
            <ellipse cx="8" cy="8" rx="2.2" ry="5" fill="none" stroke="#fff" stroke-width="1"/>
            <path d="M3 8 H13" stroke="#fff" stroke-width="1"/>
          </svg>
          vantorelectricalandcomms.example.au
        </li>
      </ul>
      <p class="reg-line"><span class="label">ABN:</span> 71829304516</p>
    </div>
    <p class="licence"><span class="label">Lic No:</span> 483027D</p>
  </section>

  <section class="card card-back" aria-label="Business card back">
    <p class="brand-name">Vantor<br>Electrical and Communications</p>
  </section>

</main>
</body>
</html>
```